We specialize in pizza, pasta and salads and are now offering TAKE & BAKE and GRAB & GO ...

Looking for either a 8.5" x 11" or similar for a instore display. WILL BE ON A SWIVELING HOLDER to catch customers attention.

**THIS IS A DOUBLE SIDED PRINT**

ONE SIDE will consist of WHAT'S FOR DINNER TONIGHT? and the following:
* Take & Bake"
* "Baked Pasta"
* Freshly made in house
* Lasagna
$13.50
- please include attached closeup picture and logo

THE OTHER SIDE will consist of
mini charcutier board.
* snack size charcutier delight *
* Enjoy the flavors of gourmet snacking, all in one convenient box!

PRICE $8.99

Winning design will be commissioned to design labels for "grab and go" for take and bake pasta, charcuterie box, pasta salads, candy etc.

Thank you and please do not hesitate to ask any questions.

www.belmaropizza.ca
www.peachnook.ca
Logo to be interchanged as they are affiliated meaning PeachNook is a brand within Belmaro pizza.

our target market is customers who have already entered our business. This is to upsel

We are in a self serve enviroment and target business people

• must be clean and catchy. We are located in a professional business community.
• Must be appealing, appetizing and utilize our website colors
• should not have any carton drawings and not be cluttered (busy)

```html
<!DOCTYPE html>
<html lang="en">
<head>
<meta charset="utf-8">
<title>Mini Charcutier Board – Belmaro Pizza</title>
<link href="https://fonts.googleapis.com/css2?family=Poppins:wght@300;700;800;900&display=swap" rel="stylesheet">
<style>
  :root {
    --brand-red: #b0252f;
    --paper: #ffffff;
    --ink: #0b0b0b;
  }
  html, body {
    margin: 0;
    padding: 0;
    overflow: hidden;
    background: var(--paper);
  }
  .flyer {
    position: relative;
    width: 928px;
    height: 1200px;
    overflow: hidden;
    background: var(--paper);
    border-left: 3px solid var(--brand-red);
    box-sizing: border-box;
    font-family: "Poppins", sans-serif;
  }
  .promo-band {
    position: absolute;
    left: 0;
    top: 44px;
    width: 928px;
    height: 1080px;
    background: var(--brand-red);
  }
  .decor-area {
    position: absolute;
    background: var(--brand-red);
  }
  .decor-board   { left: 150px; top: 44px;  width: 600px; height: 445px; }
  .decor-top     { left: 755px; top: 120px; width: 140px; height: 155px; }
  .decor-left    { left: 35px;  top: 390px; width: 190px; height: 300px; }
  .decor-bottom  { left: 685px; top: 565px; width: 185px; height: 150px; }
  .title {
    position: absolute;
    left: 194px;
    width: 534px;
    top: 106px;
    margin: 0;
    color: var(--paper);
    text-align: center;
    font-weight: 800;
    font-size: 88px;
    line-height: 82px;
    letter-spacing: -1px;
  }
  .title span { display: block; }
  .features {
    position: absolute;
    left: 268px;
    top: 535px;
    margin: 0;
    padding: 0;
    list-style: none;
    color: var(--paper);
    font-weight: 800;
    font-size: 36px;
    line-height: 54px;
    letter-spacing: -0.3px;
  }
  .features li::before {
    content: "";
    display: inline-block;
    width: 12px;
    height: 12px;
    border-radius: 50%;
    background: var(--paper);
    margin: 0 17px 6px 0;
    vertical-align: middle;
  }
  .tagline {
    position: absolute;
    left: 0;
    width: 928px;
    top: 742px;
    margin: 0;
    color: var(--paper);
    text-align: center;
    font-weight: 800;
    font-size: 37px;
    line-height: 64px;
    letter-spacing: 1.9px;
  }
  .price {
    position: absolute;
    left: 0;
    width: 928px;
    top: 893px;
    text-align: center;
    color: var(--ink);
    -webkit-text-stroke: 3px var(--paper);
    paint-order: stroke fill;
    font-weight: 900;
  }
  .price-amount {
    display: block;
    font-size: 90px;
    line-height: 90px;
    letter-spacing: -2px;
    margin-left: -62px;
  }
  .price-amount sup {
    font-size: 40px;
    vertical-align: 34px;
    margin-right: 2px;
  }
  .price-label {
    display: block;
    font-size: 34px;
    line-height: 30px;
    letter-spacing: -0.5px;
    margin-left: -34px;
    margin-top: 2px;
  }
  .brand-name {
    position: absolute;
    right: 48px;
    top: 1140px;
    margin: 0;
    color: var(--ink);
    font-weight: 300;
    font-size: 38px;
    line-height: 44px;
    letter-spacing: 1px;
  }
</style>
</head>
<body>
<main class="flyer">
  <div class="promo-band"></div>

  <div class="decor-area decor-board" role="img" aria-label="Outlined serving boards decoration behind the title"></div>
  <div class="decor-area decor-top" role="img" aria-label="Outlined cheese and cracker shapes decoration"></div>
  <div class="decor-area decor-left" role="img" aria-label="Outlined cheese and cracker shapes decoration"></div>
  <div class="decor-area decor-bottom" role="img" aria-label="Outlined cheese and cracker shapes decoration"></div>

  <h1 class="title">
    <span>mini</span>
    <span>Charcutier</span>
    <span>board</span>
  </h1>

  <ul class="features">
    <li>snack size</li>
    <li>charcutier delight</li>
  </ul>

  <p class="tagline">Enjoy the flavors of gourmet snacking,<br>all in one convenient box!</p>

  <div class="price">
    <span class="price-amount"><sup>$</sup>8.99</span>
    <span class="price-label">PRICE</span>
  </div>

  <p class="brand-name">BELMARO PIZZA</p>
</main>
</body>
</html>
```